8" x 11" One Page Flyer for Fence Installation Company

We are looking to promote our business with a new flyer that would be handed out in person to people or put at their mailbox/door at their homes. The flyer needs to be creative and attention-grabbing. I have attached some of our previous flyers and our website information. Do not call or email regarding the flyer. We want the flyer to look professional but also friendly. One page, NOT folded. You can use images from our website at www.MyBraxtonYard.com or our Facebook page at www.Facebook.com/HollowbrookRailsBKT. We are flexible with what photos you can use but there must be photos of OUR fences on the flyer. More photos specifically can also be provided. Colors need to be suitable for a flyer printed on canary yellow in color paper OR white paper.

Target Market(s)

Homeowners that need a new fence

Industry/Entity Type

Construction

Font styles to use
Sans Serif
Other font styles liked:
• HD Colton

Colors
0054AA
0677BA
7BADD7
CADEEF
E8F1F8
0094D4
00A9DD
6FCCEA
C7EBF8
E9F6FB

Requirements
Must have
• Our fence photos - mostly wood fence photos (different designs), SIZE SHOULD BE LETTER SIZE 8" x 11"
Nice to have
• A nice bible verse featured at the bottom of the flyer.
Should not have
• DO NOT COPY THE WEBSITE FORMAT, I WANT SOMETHING UNIQUE. Other people's fence photos, they must all come from our website or facebook page

```html
<!DOCTYPE html>
<html lang="en">
<head>
<meta charset="utf-8">
<title>Hollowbrook Rails – Flyer</title>
<link rel="stylesheet" href="https://fonts.googleapis.com/css2?family=Roboto:wght@700;900&family=PT+Sans:ital,wght@0,400;0,700;1,400;1,700&family=Saira:wght@600&display=swap">
<style>
  :root{
    --blue:#3d86c9;
    --blue-deep:#2f73b5;
    --orange:#e99136;
    --brown:#5a3b26;
    --ink:#222;
    --page:#ffffff;
    --stage:#e6e6e6;
  }
  html,body{margin:0;padding:0;width:1200px;height:2640px;overflow:hidden;background:var(--stage);}
  .flyer{position:absolute;left:50px;top:605px;width:1100px;height:1430px;background:var(--page);overflow:hidden;
    font-family:"PT Sans",sans-serif;color:var(--ink);box-shadow:0 10px 40px rgba(0,0,0,.18);}
  .flyer-shapes{position:absolute;left:0;top:0;width:1100px;height:1430px;}
  .brand{position:absolute;left:103px;top:78px;display:flex;align-items:center;gap:20px;}
  .brand-mark{width:72px;height:72px;background:var(--brown);}
  .brand-name{font-family:"Saira",sans-serif;font-weight:600;font-size:38px;line-height:1;color:var(--blue);margin:0;}
  .brand-phone{font-family:"Saira",sans-serif;font-weight:600;font-size:36px;line-height:1.05;color:#111;margin:0;}
  .brand-tagline{font-family:"PT Sans",sans-serif;font-weight:700;font-size:11px;margin:6px 0 0;color:#111;}
  .headline{position:absolute;left:103px;top:410px;margin:0;font-family:"Roboto",sans-serif;font-weight:900;
    font-size:86px;line-height:.94;color:#fff;letter-spacing:-1px;}
  .headline-sub{position:absolute;left:103px;top:678px;width:380px;margin:0;font-size:25px;line-height:1.2;color:#fff;}
  .why{position:absolute;left:103px;top:856px;width:360px;}
  .why h2{margin:0;font-family:"PT Sans",sans-serif;font-weight:700;font-size:31px;color:var(--blue);}
  .why-lead{margin:4px 0 22px;font-size:24px;line-height:1.2;color:var(--orange);}
  .perks{list-style:none;margin:0;padding:0;}
  .perks li{font-size:18.5px;line-height:34px;display:flex;align-items:center;gap:8px;}
  .perks svg{width:12px;height:12px;flex:none;}
  .visit{margin:16px 0 0;font-size:14.5px;line-height:1.3;width:350px;}
  .gallery{position:absolute;left:0;top:0;}
  .thumb{position:absolute;width:195px;height:150px;border-radius:10px;box-shadow:0 3px 8px rgba(0,0,0,.3);}
  .wood-a{background:linear-gradient(135deg,#6b4a2e,#cfa874 45%,#e0c08c);}
  .wood-b{background:linear-gradient(160deg,#3f5d2e,#6f8a4a 45%,#b99a6a 70%,#7c6a4a);}
  .wood-c{background:linear-gradient(160deg,#4b6b36,#a79d80 50%,#dcc79a);}
  .wood-d{background:linear-gradient(160deg,#4c5f34,#8b6a48 40%,#b68a5c);}
  .wood-e{background:linear-gradient(160deg,#3e6b30,#c9a05c 45%,#e2bf78);}
  .wood-f{background:linear-gradient(160deg,#6a5440,#bca98c 50%,#8b7a62);}
  .wood-g{background:linear-gradient(160deg,#4d6a3c,#2a2a2a 45%,#7a8a5a);}
  .location{position:absolute;left:479px;top:1008px;width:174px;height:40px;background:var(--blue);color:#fff;
    font-size:13.5px;line-height:1.1;text-align:center;padding-top:4px;box-sizing:border-box;}
  .map{position:absolute;left:459px;top:1051px;width:195px;height:146px;border-radius:8px;
    background:linear-gradient(135deg,#e9ecef,#d9dee3);box-shadow:0 3px 8px rgba(0,0,0,.25);}
  .hours{position:absolute;left:474px;top:1252px;margin:0;font-size:15px;line-height:1.6;color:var(--orange);}
  .footer-item{position:absolute;top:1385px;color:#fff;font-size:14.5px;line-height:1.25;}
  .footer-item b{display:flex;align-items:center;gap:5px;font-weight:700;}
  .footer-item svg{width:13px;height:13px;}
</style>
</head>
<body>
<main class="flyer">
  <svg class="flyer-shapes" viewBox="0 0 1100 1430">
    <defs>
      <linearGradient id="sky-field" x1="0" y1="0" x2="0" y2="1">
        <stop offset="0" stop-color="#c9d6e0"/>
        <stop offset=".25" stop-color="#7b6b4a"/>
        <stop offset=".45" stop-color="#d9c08e"/>
        <stop offset=".6" stop-color="#7a7a4a"/>
        <stop offset="1" stop-color="#a98e64"/>
      </linearGradient>
    </defs>
    <path d="M760,0 L840,0 C805,60 780,130 770,200 L715,200 C730,120 755,50 760,0Z" fill="var(--blue)"/>
    <path d="M850,0 L1100,0 L1100,200 L785,200 C800,120 820,55 850,0Z" fill="var(--orange)"/>
    <path d="M330,200 L1100,200 L1100,749 L560,749 L220,291Z" fill="url(#sky-field)" role="img" aria-label="Photo of a new wood split-rail fence with wire mesh along a brick house and lawn"/>
    <path d="M600,749 C650,830 815,830 865,749Z" fill="var(--orange)"/>
    <path d="M0,291 L150,291 C240,291 300,320 360,410 L640,780 C660,805 680,815 710,815 L0,815Z" fill="var(--blue)" stroke="#fff" stroke-width="8"/>
    <path d="M230,1430 C270,1398 290,1378 340,1378 L1100,1378 L1100,1430Z" fill="var(--blue)"/>
    <rect x="600" y="1378" width="168" height="52" fill="var(--blue-deep)"/>
    <rect x="0" y="1426" width="1100" height="4" fill="var(--blue)"/>
  </svg>

  <header class="brand">
    <div class="brand-mark"></div>
    <div>
      <p class="brand-name">Hollowbrook Rails</p>
      <p class="brand-phone">704-555-0193</p>
      <p class="brand-tagline">"Because Good Fences Make Good Neighbors"</p>
    </div>
  </header>

  <h1 class="headline">WE<br>BUILD<br>Fences....</h1>
  <p class="headline-sub">And we would love to build your fence too!</p>

  <section class="why">
    <h2>Why Choose Us?</h2>
    <p class="why-lead">Beautiful, professionally installed fencesat affordable prices!</p>
    <ul class="perks">
      <li><svg viewBox="0 0 12 12"><circle cx="6" cy="6" r="5" fill="none" stroke="#e99136" stroke-width="1.2"/><path d="M3.5,6 L5.3,7.8 L8.6,4.3" fill="none" stroke="#e99136" stroke-width="1.2"/></svg>Free Estimates</li>
      <li><svg viewBox="0 0 12 12"><circle cx="6" cy="6" r="5" fill="none" stroke="#e99136" stroke-width="1.2"/><path d="M3.5,6 L5.3,7.8 L8.6,4.3" fill="none" stroke="#e99136" stroke-width="1.2"/></svg>Professional Installation</li>
      <li><svg viewBox="0 0 12 12"><circle cx="6" cy="6" r="5" fill="none" stroke="#e99136" stroke-width="1.2"/><path d="M3.5,6 L5.3,7.8 L8.6,4.3" fill="none" stroke="#e99136" stroke-width="1.2"/></svg>Concrete in EVERY Post</li>
      <li><svg viewBox="0 0 12 12"><circle cx="6" cy="6" r="5" fill="none" stroke="#e99136" stroke-width="1.2"/><path d="M3.5,6 L5.3,7.8 L8.6,4.3" fill="none" stroke="#e99136" stroke-width="1.2"/></svg>HOA Submission Assistance</li>
      <li><svg viewBox="0 0 12 12"><circle cx="6" cy="6" r="5" fill="none" stroke="#e99136" stroke-width="1.2"/><path d="M3.5,6 L5.3,7.8 L8.6,4.3" fill="none" stroke="#e99136" stroke-width="1.2"/></svg>Lifetime Workmanship Warranty</li>
      <li><svg viewBox="0 0 12 12"><circle cx="6" cy="6" r="5" fill="none" stroke="#e99136" stroke-width="1.2"/><path d="M3.5,6 L5.3,7.8 L8.6,4.3" fill="none" stroke="#e99136" stroke-width="1.2"/></svg>Experienced Installation Teams</li>
      <li><svg viewBox="0 0 12 12"><circle cx="6" cy="6" r="5" fill="none" stroke="#e99136" stroke-width="1.2"/><path d="M3.5,6 L5.3,7.8 L8.6,4.3" fill="none" stroke="#e99136" stroke-width="1.2"/></svg>Quality Workmanship &amp; Materials</li>
      <li><svg viewBox="0 0 12 12"><circle cx="6" cy="6" r="5" fill="none" stroke="#e99136" stroke-width="1.2"/><path d="M3.5,6 L5.3,7.8 L8.6,4.3" fill="none" stroke="#e99136" stroke-width="1.2"/></svg>FREE Gate Adjustments for LIFE</li>
    </ul>
    <p class="visit">Visit our indoor &amp; outdoor showroom! Our outdoor showroom is open 24/7, while our indoor showroom and office is open</p>
  </section>

  <div class="gallery">
    <div class="thumb wood-a" style="left:463px;top:849px" role="img" aria-label="Photo of a tall wooden privacy fence with company sign"></div>
    <div class="thumb wood-b" style="left:674px;top:849px" role="img" aria-label="Photo of a wood rail fence with wire mesh"></div>
    <div class="thumb wood-c" style="left:885px;top:849px" role="img" aria-label="Photo of a wooden fence gate with arched top"></div>
    <div class="thumb wood-d" style="left:674px;top:1015px" role="img" aria-label="Photo of a wooden privacy fence beside flower beds"></div>
    <div class="thumb wood-e" style="left:885px;top:1015px" role="img" aria-label="Photo of a new dog-ear picket fence line"></div>
    <div class="thumb wood-f" style="left:674px;top:1181px" role="img" aria-label="Photo of a wooden fence gate with black hardware"></div>
    <div class="thumb wood-g" style="left:885px;top:1181px" role="img" aria-label="Photo of a black metal picket fence"></div>
  </div>
  <div class="location">418 Millbrook Rd<br>Braxton, NC 28090</div>
  <div class="map" role="img" aria-label="Street map showing the showroom location"></div>
  <p class="hours">Monday -Thurs 9AM - 3PM,<br>Friday 9AM - 1PM</p>

  <div class="footer-item" style="left:360px">
    <b><svg viewBox="0 0 13 13"><rect x="1" y="3" width="11" height="8" fill="#fff"/><path d="M1,3 L6.5,7.5 L12,3" fill="none" stroke="#3d86c9" stroke-width="1.2"/></svg>Email Address:</b>
    <span style="padding-left:18px">office@mybraxtonyard.com</span>
  </div>
  <div class="footer-item" style="left:618px">
    <b><svg viewBox="0 0 13 13"><path d="M3,1 L5,4 L4,5.5 C5,7.5 6,8.5 7.5,9 L9,8 L12,10 L10.5,12 C6,12 1,7 1,2.5Z" fill="#fff"/></svg>Call Us:</b>
    <span style="padding-left:18px">704-555-0193</span>
  </div>
  <div class="footer-item" style="left:780px">
    <b><svg viewBox="0 0 13 13"><circle cx="6.5" cy="6.5" r="5.5" fill="none" stroke="#fff" stroke-width="1.2"/><ellipse cx="6.5" cy="6.5" rx="2.4" ry="5.5" fill="none" stroke="#fff" stroke-width="1"/><path d="M1,6.5 H12" stroke="#fff" stroke-width="1"/></svg>Web</b>
    <span style="padding-left:18px">www.mybraxtonyard.com</span>
  </div>
</main>
</body>
</html>
```